Website development

Looking for a simple website, containing circa 10-15 pages of brochure-ware content for our new Cafe and Farm Shop venture.

We have a logo, designed through this site, which we think is really strong.

The Cafe and Farm Shop are all about locally sourced, high quality food served in a stunning rural location by happy, friendly staff. Great quality food and drink at sensible prices.

Initially the website needs to contain 10 or so pages of content, which ideally we would like to manage on-going (perhaps not every page, but as many pages as the budget will allow). We want to make sure that the website stays fresh and current and so we want a basic CMS to keep the text areas updated.

We would also like a simple data capture page, so that we can start to generate a database of email addresses for our on-going marketing efforts. Any thoughts around a basic CRM tool gratefully received.

The creative brief can take some inspiration from the logo, but should be bright, clean, welcoming and engaging. Not too over-bearing with colours or content. Fun, easy and interesting to use with all the text and image information clearly displayed.

We don't currently have any imagery beyond the logo, and would like to use as much free stock photography and imagery as possible. If needs be we can take some good quality pictures and provide them.

We're in the process of purchasing the URL(s) at present and will supply them in due course, but they will be based around the trading name.

If you have any more questions please do not hesitate to contact me.

Many thanks
Owen

Industry/Entity Type

Cafe

```html
<!DOCTYPE html>
<html lang="en">
<head>
<meta charset="utf-8">
<title>The Willow Barn – Cafe and Farm Shop</title>
<link href="https://fonts.googleapis.com/css2?family=Oswald:wght@400;500&family=Open+Sans:wght@400;600;700&display=swap" rel="stylesheet">
<style>
  :root {
    --page-bg: #f4f6f7;
    --header-top: #dfeaf1;
    --header-bottom: #ffffff;
    --brand-green: #2f5a34;
    --teal: #2bb3bd;
    --ink: #1f2a26;
    --text: #6b7270;
    --heading: #3c4a56;
    --nav-active: #dcdfe1;
    --sky: #a9cde4;
    --field-light: #b7d86a;
    --field-dark: #4f8a2a;
    --footer-bg: #e6e9eb;
    --footer-line: #d3d7da;
    --bar-bg: #dfe2e4;
    --white: #ffffff;
  }
  * { box-sizing: border-box; margin: 0; padding: 0; }
  html, body { width: 1200px; height: 901px; overflow: hidden; }
  body {
    background: var(--page-bg);
    font-family: "Open Sans", Arial, sans-serif;
    color: var(--text);
  }
  .site { position: relative; width: 1200px; height: 901px; }
  .container { width: 1000px; margin: 0 auto; position: relative; }

  /* Header */
  .site-header {
    height: 150px;
    background: linear-gradient(180deg, var(--header-top) 0%, var(--header-bottom) 100%);
  }
  .site-header .container { height: 150px; }
  .brand { position: absolute; left: 0; top: 34px; display: flex; align-items: center; gap: 10px; }
  .brand-mark { width: 14px; height: 14px; border-radius: 50%; background: var(--teal); }
  .brand-name { font-weight: 600; font-size: 30px; color: var(--brand-green); line-height: 1; }
  .brand-tagline {
    position: absolute; left: 24px; top: 76px;
    font-size: 11px; letter-spacing: 3px; text-transform: uppercase;
    color: var(--brand-green); font-weight: 600;
  }
  .social { position: absolute; right: 0; top: 36px; display: flex; gap: 6px; }
  .social span { width: 14px; height: 14px; background: #7b8da3; border-radius: 2px; }
  .social span:nth-child(3) { background: #c9473f; }
  .main-nav { position: absolute; right: 0; top: 102px; display: flex; gap: 4px; }
  .main-nav a {
    font-size: 13px; font-weight: 600; color: var(--heading);
    text-decoration: none; padding: 8px 10px; border-radius: 2px;
  }
  .main-nav a.is-active { background: var(--nav-active); }

  /* Hero */
  .hero { position: relative; height: 380px; overflow: hidden; }
  .hero-image {
    position: absolute; inset: 0;
    background:
      linear-gradient(180deg, var(--sky) 0%, #d8e9ef 28%, var(--field-light) 40%, #8fbf49 65%, var(--field-dark) 100%);
  }
  .hero-wave { position: absolute; left: 0; bottom: 0; width: 1200px; height: 120px; }
  .hero-title {
    position: absolute; left: 100px; top: 108px;
    font-family: "Oswald", "Arial Narrow", sans-serif; text-transform: uppercase; line-height: 1.05;
  }
  .hero-title .line-one { display: block; font-size: 62px; font-weight: 500; color: var(--teal); }
  .hero-title .line-two { display: block; font-size: 52px; font-weight: 400; color: var(--ink); }

  /* Content */
  .content { height: 190px; background: var(--white); }
  .content .container { display: flex; gap: 50px; padding-top: 10px; }
  .content-block { width: 475px; }
  .content-block h2 { font-size: 14px; font-weight: 700; color: var(--heading); margin-bottom: 8px; }
  .content-block p { font-size: 11px; line-height: 1.5; margin-bottom: 10px; }

  /* Footer */
  .site-footer {
    height: 140px;
    background: linear-gradient(180deg, var(--footer-bg), #f1f3f4);
    border-top: 1px solid var(--footer-line);
  }
  .site-footer .container { display: flex; padding-top: 18px; }
  .footer-col { width: 250px; }
  .footer-col h3 { font-size: 13px; font-weight: 700; color: var(--heading); margin-bottom: 6px; }
  .footer-col ul { list-style: none; }
  .footer-col li { font-size: 10px; line-height: 1.45; }
  .footer-col .phone { margin-top: 14px; font-size: 11px; }

  .bottom-bar { height: 41px; background: var(--bar-bg); border-top: 1px solid var(--footer-line); }
  .bottom-bar .container { display: flex; align-items: center; gap: 40px; height: 41px; font-size: 10px; }
  .bottom-bar .mini-brand { font-weight: 600; color: var(--brand-green); font-size: 12px; }
</style>
</head>
<body>
<div class="site">
  <header class="site-header">
    <div class="container">
      <div class="brand">
        <span class="brand-mark"></span>
        <span class="brand-name">The Willow Barn</span>
      </div>
      <div class="brand-tagline">Cafe and Farm Shop</div>
      <div class="social"><span></span><span></span><span></span><span></span></div>
      <nav class="main-nav">
        <a href="#" class="is-active">Home</a>
        <a href="#">About Us</a>
        <a href="#">News</a>
        <a href="#">Events</a>
        <a href="#">Coffe Shop</a>
        <a href="#">Farm Shop</a>
        <a href="#">Contact Us</a>
      </nav>
    </div>
  </header>

  <section class="hero">
    <div class="hero-image" role="img" aria-label="Photo of a sunny green meadow under a blue sky, with a yellow songbird on a branch and a cup of coffee with coffee beans"></div>
    <svg class="hero-wave" viewBox="0 0 1200 120" preserveAspectRatio="none" aria-hidden="true">
      <path d="M0 70 C 250 20, 420 20, 620 60 S 1000 110, 1200 40 L1200 120 L0 120 Z" fill="#ffffff" opacity="0.55"/>
      <path d="M0 95 C 260 50, 450 50, 640 85 S 1000 125, 1200 75 L1200 120 L0 120 Z" fill="#ffffff"/>
    </svg>
    <h1 class="hero-title">
      <span class="line-one">Lorem Ipsum,</span>
      <span class="line-two">Dolor Sit Amet</span>
    </h1>
  </section>

  <main class="content">
    <div class="container">
      <article class="content-block">
        <h2>About Us</h2>
        <p>Lorem ipsum dolor sit amet, consectetur adipiscing elit. Vivamus egestas velit at elit viverra luctus. Lorem ipsum dolor sit amet, consectetur adipiscing elit. Vestibulum viverra aliquet arcu, ac lobortis enim volutpat at. Integer sem turpis, mattis ut imperdiet rutrum.</p>
      </article>
      <article class="content-block">
        <h2>News</h2>
        <p>Lorem ipsum dolor sit amet, consectetur adipiscing elit. Vivamus egestas velit at elit viverra luctus. Lorem ipsum dolor sit amet.</p>
        <p>Vestibulum viverra aliquet arcu, ac lobortis enim volutpat at. Integer sem turpis, mattis ut imperdiet rutrum.</p>
      </article>
    </div>
  </main>

  <footer class="site-footer">
    <div class="container">
      <div class="footer-col">
        <h3>About Us</h3>
        <ul><li>Lorem ipsum</li><li>Dolor sit amet</li><li>Lorem ipsum</li><li>Dolor sit amet</li><li>Lorem ipsum</li><li>Dolor sit amet</li></ul>
      </div>
      <div class="footer-col">
        <h3>Coffe Shop</h3>
        <ul><li>Lorem ipsum</li><li>Dolor sit amet</li><li>Lorem ipsum</li><li>Dolor sit amet</li><li>Lorem ipsum</li><li>Dolor sit amet</li></ul>
      </div>
      <div class="footer-col">
        <h3>Farm Shop</h3>
        <ul><li>Lorem ipsum</li><li>Dolor sit amet</li><li>Lorem ipsum</li><li>Dolor sit amet</li><li>Lorem ipsum</li><li>Dolor sit amet</li></ul>
      </div>
      <div class="footer-col">
        <h3>Contact Us</h3>
        <ul><li>Lorem ipsum</li><li>Dolor sit amet</li><li>Lorem ipsum</li></ul>
        <p class="phone">+00 0000 0000</p>
      </div>
    </div>
  </footer>

  <div class="bottom-bar">
    <div class="container">
      <span>© 2011 All Rights Reserved</span>
      <span class="mini-brand">The Willow Barn</span>
    </div>
  </div>
</div>
</body>
</html>
```